Multiple Airplane Listing Design for email blast

Need a graphic to be loaded to Constant Contact to advertise multiple airplanes for sale. The title should say:

Meridane Focused: Start your search here!

The under each photo it should say the model and the serial # (name of the picture).

317-0946 - Meridane LV
317A-0583 - Meridane LV2+
317B-0639 Meridane LV3
317C-0087 - Meridane LV4 (Pending)
492-0735 - Meridane Harbor (Pending)
864-0519 - Meridane Q (Coming Soon)

The design should match our website with logo and colors. www.skylorn-avia.example

```html
<!DOCTYPE html>
<html lang="en">
<head>
<meta charset="utf-8">
<title>Skylorn Avia – Meridane Listings</title>
<link href="https://fonts.googleapis.com/css2?family=Montserrat:wght@400;500;600&family=Source+Sans+3:wght@400&display=swap" rel="stylesheet">
<style>
  :root{
    --page:#efefef;
    --card:#ffffff;
    --brand:#3c5398;
    --brand-deep:#1f3163;
    --navy:#1b2547;
    --ink:#2b2f3a;
    --muted:#c9ced8;
    --link:#e6479a;
    --hero-photo-a:#2a3148;
    --hero-photo-b:#0f1424;
  }
  *{box-sizing:border-box;margin:0;padding:0}
  html,body{width:710px;height:1200px;overflow:hidden;background:var(--page)}
  body{position:relative;font-family:"Montserrat",Arial,sans-serif;color:var(--ink)}
  .abs{position:absolute}
  .notice{top:22px;left:0;width:710px;text-align:center;font:400 12.5px "Source Sans 3",Arial,sans-serif;color:#333}
  .notice a{color:var(--link);text-decoration:none;border-bottom:1px solid var(--link)}
  .notice--bottom{top:1158px;font-size:11.5px}

  .sheet{left:34px;top:51px;width:648px;height:1095px;background:var(--card);border-top:4px solid var(--brand-deep);box-shadow:0 1px 3px rgba(0,0,0,.15)}
  .rule{background:var(--muted);height:1px}

  .brand{display:flex;align-items:center;gap:8px;color:var(--brand)}
  .brand__dot{width:30px;height:30px;border-radius:50%;background:var(--brand)}
  .brand__name{font-weight:500;font-size:13px;letter-spacing:4px}
  .brand__tag{font-size:6.5px;letter-spacing:.3px;color:#444;margin-top:3px}

  .call{left:396px;top:50px;display:flex;gap:6px;align-items:center;color:var(--brand);font-size:10px;line-height:14px}
  .dateline{left:558px;top:52px;font-size:8px;color:#333;text-align:right;width:56px}
  .socials{display:flex;gap:4px}
  .socials span{width:11px;height:11px;border-radius:50%;background:var(--navy)}
  .socials--top{left:568px;top:66px}

  .search-bump{left:322px;top:64px}
  .banner{left:32px;top:91px;width:587px;height:66px;background:var(--brand);color:#fff;font-size:21px;font-weight:400;display:flex;align-items:center;justify-content:center;letter-spacing:.2px}
  .hero-photo{left:33px;top:159px;width:395px;height:212px;background:radial-gradient(ellipse at 55% 50%,#6b7286 0%,var(--hero-photo-a) 35%,var(--hero-photo-b) 100%)}
  .hero-panel{left:428px;top:159px;width:191px;height:212px;background:var(--brand);color:#fff;padding:54px 0 0 12px}
  .hero-panel h2{font-weight:400;font-size:14.5px;margin-bottom:18px;white-space:nowrap}
  .hero-panel p{font-size:10px;line-height:17px}
  .btn-dark{display:inline-block;margin-top:12px;background:var(--brand-deep);color:#fff;font-size:8.5px;font-weight:500;padding:11px 10px;border-radius:2px}

  .about-mark{left:86px;top:417px;width:72px;height:52px;display:flex;align-items:center;justify-content:center;color:var(--brand);font-size:13px;font-weight:600;letter-spacing:1px}
  .about-divider{left:167px;top:412px;width:1px;height:62px;background:var(--muted)}
  .about-text{left:182px;top:410px;width:400px;font-size:8.4px;line-height:12.8px;color:#222}
  .about-accent{height:1px;background:var(--muted)}

  .section-title{left:0;top:523px;width:648px;display:flex;justify-content:center;align-items:center;gap:5px;font-size:10px;font-weight:600;color:var(--navy);letter-spacing:.3px}
  .section-title__dots{left:290px;top:540px;width:84px;border-top:2px dotted #9aa3bd}

  .product{top:576px;width:188px}
  .product__photo{height:127px;position:relative}
  .product__photo--day{background:linear-gradient(#5f8fd0 0%,#a9c4e6 50%,#8c8f95 65%,#6d6f74 100%)}
  .product__photo--clear{background:linear-gradient(#2d66b8 0%,#6fa0dd 55%,#9aa2a9 66%,#7a7f86 100%)}
  .product__photo--night{background:linear-gradient(#3a2a20 0%,#5d4330 45%,#1b1b1f 70%,#101014 100%)}
  .product__strip{position:absolute;right:0;top:0;width:34px;height:100%;background:rgba(60,83,152,.85);display:flex;flex-direction:column;align-items:center;justify-content:space-around;padding:8px 0}
  .product__title{margin:15px 0 0 13px;font-size:12px;font-weight:600;color:var(--brand);white-space:nowrap}
  .product__body{margin:8px 0 0 13px;font-size:7.9px;line-height:12.8px;color:#222;width:172px;letter-spacing:-.1px}
  .product__more{margin:8px 0 0 13px;font-size:8.4px;font-weight:600;color:var(--navy)}

  .btn-more{left:274px;top:819px;width:95px;height:34px;background:var(--brand);color:#fff;font-size:10.5px;font-weight:600;display:flex;align-items:center;justify-content:center;gap:5px;border-radius:1px}

  .footer{left:0;top:889px;width:648px;height:206px;background:var(--brand);color:#fff;border-bottom:5px solid var(--brand-deep)}
  .footer .brand{color:#fff;justify-content:center}
  .footer .brand__dot{background:#fff;width:22px;height:22px}
  .footer .brand__name{font-size:9px;letter-spacing:3px}
  .footer .socials span{background:#fff;width:12px;height:12px}
  .contact{top:94px;font-size:7.5px;line-height:11.5px;font-weight:500}
  .contact__icon{display:block;margin-bottom:9px}
  .contact-sep{top:92px;width:0;height:58px;border-left:1px dotted rgba(255,255,255,.6)}
  .copyright{left:0;top:171px;width:648px;display:flex;justify-content:center;align-items:center;gap:7px;font-size:10px;font-weight:600}
</style>
</head>
<body>
  <p class="abs notice">Having Problems viewing this email? <a href="#">Click here</a> to view in browser.</p>

  <main class="abs sheet">
    <div class="abs rule" style="left:40px;top:19px;width:574px"></div>

    <header class="abs brand" style="left:18px;top:43px">
      <span class="brand__dot"></span>
      <div>
        <div class="brand__name">SKYLORN AVIA</div>
        <div class="brand__tag">Meridane Focused.&nbsp; Client Driven.</div>
      </div>
    </header>

    <div class="abs call">
      <svg width="26" height="26" viewBox="0 0 26 26" aria-hidden="true"><circle cx="13" cy="13" r="11.5" fill="none" stroke="var(--navy)" stroke-width="1.6"/><path d="M9 7.5c-1 1-1 3 1 6s4.5 5 6 5l1.5-1.5-2.2-2-1.3.8c-1-.6-2.4-2-3-3l.8-1.3-2-2.2z" fill="var(--navy)"/></svg>
      <div>Call Us Now:<br>(480) 555-0142</div>
    </div>
    <div class="abs dateline">1st Nov, 2015</div>
    <div class="abs socials socials--top" aria-label="Social links"><span></span><span></span><span></span><span></span></div>

    <svg class="abs search-bump" width="90" height="30" viewBox="0 0 90 30" aria-hidden="true">
      <path d="M0 30c4-10 12-14 20-14 3-9 13-15 25-15s22 6 25 15c8 0 16 4 20 14z" fill="var(--brand)"/>
      <circle cx="43" cy="17" r="6" fill="none" stroke="#fff" stroke-width="1.5"/>
      <path d="M47.5 21.5l4 4" stroke="#fff" stroke-width="1.8" stroke-linecap="round"/>
    </svg>
    <h1 class="abs banner">Meridane Focused: Start your search here!</h1>

    <div class="abs hero-photo" role="img" aria-label="Photograph of a white business jet parked on a dark apron at night"></div>
    <section class="abs hero-panel">
      <h2>317-0946 - Meridane LV</h2>
      <p>AFTT 2100<br>Serial: 317-0342</p>
      <span class="btn-dark">Details more›</span>
    </section>

    <div class="abs about-accent" style="left:414px;top:406px;width:34px"></div>
    <div class="abs about-accent" style="left:578px;top:406px;width:34px"></div>
    <div class="abs about-mark">SKYLORN</div>
    <div class="abs about-divider"></div>
    <p class="abs about-text">Skylorn Avia is an aircraft sales and acquisition firm specializing in the Meridane Family. Our industry leading market research, creative and innovative marketing and our powerful network of contacts makes Skylorn Avia the ideal choice when buying or selling a Meridane. Our team offers over 75 years of combined experience, a strong reputation of integrity and a vast knowledge of the industry. Meridane Focused. Client Driven.</p>
    <div class="abs rule" style="left:136px;top:499px;width:370px"></div>

    <h3 class="abs section-title">
      <svg width="14" height="13" viewBox="0 0 14 13" aria-hidden="true"><path d="M13 1L1 6l4 1.5L6.5 12 8.5 8.5zM5 7.5L13 1" fill="none" stroke="var(--navy)" stroke-width="1"/></svg>
      SEE PRODUCTS:
    </h3>
    <div class="abs section-title__dots"></div>

    <article class="abs product" style="left:30px">
      <div class="product__photo product__photo--day" role="img" aria-label="Photograph of a white jet on a concrete ramp under a cloudy blue sky">
        <div class="product__strip"><svg width="16" height="8"><path d="M1 5h13l1-2-4 .5-3-3H6l1.5 3H3L2 2H1z" fill="none" stroke="#fff" stroke-width=".8"/></svg><svg width="16" height="16"><circle cx="8" cy="8" r="7.5" fill="#fff"/><rect x="5" y="4" width="6" height="8" fill="none" stroke="var(--brand)"/></svg><svg width="14" height="14"><rect x="1" y="2" width="12" height="8" fill="none" stroke="#fff"/><path d="M7 10v3" stroke="#fff"/></svg></div>
      </div>
      <h4 class="product__title">317B-0639 Meridane LV3</h4>
      <p class="product__body">Lorem ipsum dolor sit amet, sectetur adipisicing elit, sed do eiusmod tempor incididunt ut labore et dolore ma........</p>
      <p class="product__more">Read More››</p>
    </article>

    <article class="abs product" style="left:230px">
      <div class="product__photo product__photo--clear" role="img" aria-label="Photograph of a white jet on a runway under a clear blue sky">
        <div class="product__strip"><svg width="16" height="8"><path d="M1 5h13l1-2-4 .5-3-3H6l1.5 3H3L2 2H1z" fill="none" stroke="#fff" stroke-width=".8"/></svg><svg width="16" height="16"><circle cx="8" cy="8" r="7.5" fill="#fff"/><rect x="5" y="4" width="6" height="8" fill="none" stroke="var(--brand)"/></svg><svg width="14" height="14"><rect x="1" y="2" width="12" height="8" fill="none" stroke="#fff"/><path d="M7 10v3" stroke="#fff"/></svg></div>
      </div>
      <h4 class="product__title">317B-0639 Meridane LV3</h4>
      <p class="product__body">Lorem ipsum dolor sit amet, sectetur adipisicing elit, sed do eiusmod tempor incididunt ut labore et dolore ma........</p>
      <p class="product__more">Read More››</p>
    </article>

    <article class="abs product" style="left:429px">
      <div class="product__photo product__photo--night" role="img" aria-label="Photograph of a white jet on the tarmac at dusk with a city skyline behind">
        <div class="product__strip"><svg width="16" height="8"><path d="M1 5h13l1-2-4 .5-3-3H6l1.5 3H3L2 2H1z" fill="none" stroke="#fff" stroke-width=".8"/></svg><svg width="16" height="16"><circle cx="8" cy="8" r="7.5" fill="#fff"/><rect x="5" y="4" width="6" height="8" fill="none" stroke="var(--brand)"/></svg><svg width="14" height="14"><rect x="1" y="2" width="12" height="8" fill="none" stroke="#fff"/><path d="M7 10v3" stroke="#fff"/></svg></div>
      </div>
      <h4 class="product__title">317B-0639 Meridane LV3</h4>
      <p class="product__body">Lorem ipsum dolor sit amet, sectetur adipisicing elit, sed do eiusmod tempor incididunt ut labore et dolore ma........</p>
      <p class="product__more">Read More››</p>
    </article>

    <div class="abs btn-more">
      <svg width="13" height="12" viewBox="0 0 14 13" aria-hidden="true"><path d="M13 1L1 6l4 1.5L6.5 12 8.5 8.5zM5 7.5L13 1" fill="none" stroke="#fff" stroke-width="1.1"/></svg>
      SEE MORE
    </div>

    <footer class="abs footer">
      <div class="abs brand" style="left:0;top:18px;width:648px">
        <span class="brand__dot"></span>
        <span class="brand__name">SKYLORN AVIA</span>
      </div>
      <div class="abs socials" style="left:290px;top:56px;gap:6px" aria-label="Social links"><span></span><span></span><span></span><span></span></div>

      <div class="abs contact" style="left:155px">
        <svg class="contact__icon" style="margin-left:31px" width="10" height="13" viewBox="0 0 10 13" aria-hidden="true"><path d="M5 12.5S1 7.5 1 5a4 4 0 018 0c0 2.5-4 7.5-4 7.5z" fill="#fff"/><circle cx="5" cy="5" r="1.5" fill="var(--brand)"/></svg>
        Halvorsen Diensten<br>Kerkstraat 8<br>2041 KT Veldmoor
      </div>
      <div class="abs contact-sep" style="left:304px"></div>
      <div class="abs contact" style="left:323px">
        <svg class="contact__icon" style="margin-left:52px" width="14" height="12" viewBox="0 0 14 12" aria-hidden="true"><path d="M1 4c0-2 12-2 12 0v1.5H10V4H4v1.5H1z" fill="#fff"/><path d="M3 6h8l1.5 5h-11z" fill="#fff"/><circle cx="7" cy="8.5" r="1.4" fill="var(--brand)"/></svg>
        Tel: +31 (0) 200555018
      </div>
      <div class="abs contact-sep" style="left:471px"></div>
      <div class="abs contact" style="left:491px">
        <svg class="contact__icon" style="margin-left:22px" width="14" height="10" viewBox="0 0 14 10" aria-hidden="true"><rect x=".5" y=".5" width="13" height="9" fill="none" stroke="#fff"/><path d="M.5.5L7 6 13.5.5" fill="none" stroke="#fff"/></svg>
        info@halvorsen.example
      </div>

      <div class="abs copyright">
        <svg width="14" height="14" viewBox="0 0 14 14" aria-hidden="true"><path d="M13 1c-1-1-2.5 0-3.5 1L7.5 4 2 2.5 1 3.5 5.5 6.5 3.5 9 1.5 8.5.5 9.5l2.5 1.5 1.5 2.5 1-1-.5-2 2.5-2 3 4.5 1-1-1.5-5.5 2-2c1-1 2-2.5 1-3.5z" fill="#fff"/></svg>
        © 2014 SKYLORN AVIA. All Rights Reserved.
      </div>
    </footer>
  </main>

  <p class="abs notice notice--bottom">You are receiving this email because you subcribed at www.skylorn-news.example. To unsubscribe, <a href="#">click here</a></p>
</body>
</html>
```